Pagina Casalúmen

The Casalúmen is a company dealing with leasing and selling real estate. The current site can be accessed at www.casalumen.com.br. We intend to redesign the look of the site and for that we would like to redesign the home page and the page with information and pictures of the property. The homepage should maintain the characteristics of the current common design simple, short and straightforward. The page with the data of the properties should be accessed with two changes page as it is currently running. The search from the map by region and should be maintained.
The page containing the information of the property will provide a total of 15 small pictures that when clicked will appear in larger size. The colors to be used should be orange, blue, black and white. The map can be maintained in the current colors.
Updates

Payment guaranteed. Deadline for submission of designs April 27.

Industry/Entity Type

Real Estate

Requirements
Must have
• Search by map regions and search box
address
keep colors from the current page
phones
clean look
Nice to have
• clean look
Should not have
• We like the current page. We just want to make it compatible with modern and new design trends and monitors.

```html
<!DOCTYPE html>
<html lang="pt-BR">
<head>
<meta charset="utf-8">
<title>Casalúmen — Imóveis</title>
<link href="https://fonts.googleapis.com/css2?family=Source+Sans+3:ital,wght@0,400;0,600;0,700;1,600&display=swap" rel="stylesheet">
<style>
:root{
  --orange:#f08a2b;
  --orange-dark:#e07a1c;
  --purple:#4b4668;
  --purple-deep:#3f3a5c;
  --ink:#55535a;
  --text:#727176;
  --button:#3b3b3f;
  --header-bg:#f8f1ec;
  --page-bg:#f4f1ee;
  --footer-bg:#f6f4f2;
  --rule:#dcd8d4;
  --white:#ffffff;
}
*{box-sizing:border-box;margin:0;padding:0}
html,body{width:915px;height:1200px;overflow:hidden}
body{position:relative;background:var(--page-bg);font-family:"Source Sans 3",Arial,sans-serif;color:var(--text)}
.abs{position:absolute}

.site-header{left:0;top:0;width:915px;height:125px;background:var(--header-bg)}
.brand{left:90px;top:38px;display:flex;align-items:center;gap:10px}
.brand-mark{width:22px;height:22px;background:var(--orange)}
.brand-name{font-size:34px;font-weight:700;color:var(--purple);letter-spacing:-.5px}
.contact{right:93px;top:34px;text-align:right;font-size:14px;line-height:26px;color:#6a6870}

.main-nav{left:90px;top:108px;width:733px;height:35px;background:var(--orange);display:flex;justify-content:space-between;align-items:center;padding:0 12px 0 12px;z-index:3}
.main-nav a{color:var(--white);font-size:10.5px;font-weight:600;text-decoration:none;text-transform:uppercase}

.hero{left:0;top:125px;width:915px;height:390px;background:linear-gradient(180deg,#2f6fc1 0%,#5d97d6 45%,#b07a4e 62%,#8a4e2a 100%)}
.hero-wall{left:0;top:125px;width:380px;height:390px;background:linear-gradient(90deg,#d9d4cc,#f1ede8)}
.dots{left:702px;top:495px;display:flex;gap:6px}
.dots span{width:9px;height:9px;border-radius:50%;background:#8a7564}
.dots span.on{background:var(--orange)}

.search-panel{left:90px;top:168px;width:275px;height:330px;background:var(--purple);padding:12px 24px 0;color:var(--white);z-index:2}
.panel-title{font-size:16px;font-weight:600;text-transform:uppercase}
.modes{display:flex;gap:14px;font-size:11px;margin:8px 0 0 3px;align-items:center}
.modes label{display:flex;align-items:center;gap:5px}
.radio{width:9px;height:9px;border-radius:50%;background:#ddd;border:2px solid #ddd}
.radio.on{background:var(--purple);border-color:#cfd6ee;box-shadow:inset 0 0 0 1px #fff}
.field{background:var(--white);color:#555;font-size:11px;height:27px;line-height:27px;padding:0 6px}
.search-field{margin-top:11px;width:229px}
.row{display:flex;justify-content:space-between;margin-top:11px;width:229px}
.select{width:130px;display:flex;justify-content:space-between;align-items:center}
.select i{width:12px;height:12px;border:1px solid #888;font-style:normal;font-size:7px;line-height:10px;text-align:center}
.search-btn{width:70px;height:27px;background:var(--purple-deep);border:1px solid #6a6590;font-size:12px;text-align:center;line-height:25px;text-transform:uppercase}
.region-title{margin-top:14px}
.region-map{position:absolute;left:16px;top:177px;width:244px;height:145px;background:linear-gradient(135deg,#7fb6dc,#9fd0ea 50%,#e9c894)}

.section-title{font-size:15px;font-weight:600;color:var(--ink);text-transform:uppercase}
.section-title em{font-style:normal;color:var(--orange)}
.photo{background:#7ea35a}
.lede{font-size:8.5px;font-weight:600;font-style:italic;color:var(--purple);text-transform:uppercase;line-height:11px}
.body-copy{font-size:8.5px;line-height:13px;text-align:justify;color:var(--text)}
.btn{height:22px;line-height:22px;padding:0 6px;background:var(--button);color:var(--white);font-size:8.5px;text-transform:uppercase}
.btn.purple{background:var(--purple);padding:0 7px;font-size:9px;height:23px;line-height:23px}

.divider{left:90px;top:784px;width:733px;height:4px;background:radial-gradient(ellipse at center,#c9c4bf 0%,rgba(201,196,191,0) 70%)}
.rule{left:90px;top:837px;width:733px;height:1px;background:var(--rule)}
.pager{left:793px;top:812px;display:flex;gap:3px}
.pager span{width:12px;height:12px;border:1px solid #ccc;background:#f7f5f3;font-size:8px;line-height:10px;text-align:center;color:#999}

.card{top:845px;width:168px}
.card .photo{height:126px}
.card h3{font-size:12.5px;font-weight:600;color:var(--purple);margin:10px 0 6px}
.card .body-copy{padding:0 0 0 1px}
.card .btn{display:inline-block;margin-top:9px}

.site-footer{left:0;top:1122px;width:915px;height:78px;background:var(--footer-bg);border-top:1px solid #e3dfdb}
.address{left:92px;top:1134px;font-size:8.5px;line-height:14px;color:#6e6d72;text-transform:uppercase}
.social{left:673px;top:1136px;display:flex;gap:2px}
.social span{width:24px;height:24px;border-radius:50%;background:#aaa8a6}
.copyright{right:92px;top:1174px;font-size:9.5px;color:#8a888c}
.edition{left:887px;top:1148px;font-size:9px;color:#8a888c}
</style>
</head>
<body>

<header class="abs site-header">
  <div class="abs brand"><span class="brand-mark"></span><span class="brand-name">Casalúmen</span></div>
  <div class="abs contact">Phone: 55310-240<br>Fax: (48) 3555-2917</div>
</header>

<div class="abs hero" role="img" aria-label="Rooftop terrace with wooden deck, palm plants and sea view between tall buildings"></div>
<div class="abs hero-wall" role="img" aria-label="White wall of the terrace building"></div>
<div class="abs dots"><span class="on"></span><span></span><span></span></div>

<nav class="abs main-nav">
  <a href="#">Home</a><a href="#">Location</a><a href="#">Restricted Area</a><a href="#">List Your Property</a><a href="#">Owner Info</a><a href="#">Information for Tenant</a><a href="#">Contact Us</a>
</nav>

<section class="abs search-panel">
  <h2 class="panel-title">Search for properties</h2>
  <div class="modes"><label><span class="radio on"></span>TO BUY</label><label><span class="radio"></span>RENT</label></div>
  <div class="field search-field">Search here</div>
  <div class="row"><div class="field select">North <i>▼</i></div><div class="search-btn">Search</div></div>
  <h2 class="panel-title region-title">Search property by region</h2>
  <div class="region-map" role="img" aria-label="Regional map of the island and bay for choosing a search area"></div>
</section>

<section>
  <h2 class="abs section-title" style="left:92px;top:530px">Welcome to <em>Casalúmen</em></h2>
  <div class="abs photo" style="left:92px;top:564px;width:204px;height:163px;background:linear-gradient(180deg,#3d78c9,#9aa7b0 45%,#6f8e4a)" role="img" aria-label="Two-storey brick house with garage and palm tree"></div>
  <p class="abs lede" style="left:302px;top:565px;width:270px">Consectetur adipisicing elit, sed do eiusmod tempor incidi-dunt ut labore et dolore magna aliqua.</p>
  <p class="abs body-copy" style="left:302px;top:598px;width:270px">consectetur adipisicing elit, sed do eiusmod tempor incididunt ut labore et dolore magna aliqua. Ut enim ad minim veniam, quis nostrud exercitation ullamco laboris nisi ut aliquip ex ea commodo consequat. Duis aute irure dolor in reprehenderit in voluptate velit esse cillum dolore eu fugiat nullaconsectetur adipisicing elit, sed do eiusmod tempor incididunt ut labore et dolore magna aliqua.</p>
  <p class="abs body-copy" style="left:302px;top:689px;width:270px;text-align:left">Ut enim ad minim veniam, quis nostrud exercitation ullamco laboris nisi ut aliquip ex ea commodo consequat. Duis aute irure dolor in reprehen-derit in voluptate velit esse cillum dolore eu fugiat nulla</p>
  <div class="abs btn" style="left:91px;top:740px">Read more</div>

  <h2 class="abs section-title" style="left:595px;top:530px">Recent project news</h2>
  <div class="abs photo" style="left:595px;top:567px;width:228px;height:97px;background:linear-gradient(180deg,#2e63b4,#d2a24e 50%,#4f8a3c)" role="img" aria-label="Yellow villa with swimming pool and garden"></div>
  <p class="abs body-copy" style="left:595px;top:670px;width:228px;text-align:left">consectetur adipisicing elit, sed do eiusmod tempor incidi-dunt ut labore et dolore magna aliqua.</p>
  <p class="abs body-copy" style="left:595px;top:703px;width:228px;text-align:left;line-height:11px">Ut enim ad minim veniam, quis nostrud exercitation ullamco laboris nisi ut aliquip ex ea commodo consequat. Duis aute irure dolor in reprehenderit in voluptate</p>
  <div class="abs btn" style="left:595px;top:740px">Read more</div>
</section>

<div class="abs divider"></div>

<section>
  <h2 class="abs section-title" style="left:92px;top:808px">Featured properties</h2>
  <div class="abs pager"><span>‹</span><span>›</span></div>
  <div class="abs rule"></div>

  <article class="abs card" style="left:90px">
    <div class="photo" style="background:linear-gradient(180deg,#f2e4ea,#c8b48e 55%,#6f9a45)" role="img" aria-label="Beige two-storey family house"></div>
    <h3>consectetur adipisicing</h3>
    <p class="body-copy">consectetur adipisicing elit, sed do eiusmod tempor incididunt ut labore et dolore magna aliqua. Ut enim ad minim veniam, quis nostrud exercitation ullamco laboris nisi ut a</p>
    <div class="btn purple">More details</div>
  </article>
  <article class="abs card" style="left:278px">
    <div class="photo" style="background:linear-gradient(180deg,#e9eef2,#a9b3bd 45%,#4d7a35)" role="img" aria-label="White Victorian house with porch and garden"></div>
    <h3>consectetur adipisicing</h3>
    <p class="body-copy">consectetur adipisicing elit, sed do eiusmod tempor incididunt ut labore et dolore magna aliqua. Ut enim ad minim veniam, quis nostrud exercitation ullamco laboris nisi ut a</p>
    <div class="btn purple">More details</div>
  </article>
  <article class="abs card" style="left:466px">
    <div class="photo" style="background:linear-gradient(180deg,#3c86d0,#a6c4e0 40%,#7a6f72 70%,#e6e2e0)" role="img" aria-label="Pink cottage with white picket fence"></div>
    <h3>consectetur adipisicing</h3>
    <p class="body-copy">consectetur adipisicing elit, sed do eiusmod tempor incididunt ut labore et dolore magna aliqua. Ut enim ad minim veniam, quis nostrud exercitation ullamco laboris nisi ut a</p>
    <div class="btn purple">More details</div>
  </article>
  <article class="abs card" style="left:655px">
    <div class="photo" style="background:linear-gradient(180deg,#4a88c9,#cfc7bd 45%,#3f6a2e)" role="img" aria-label="Raised white house with red stairs and tropical plants"></div>
    <h3>consectetur adipisicing</h3>
    <p class="body-copy">consectetur adipisicing elit, sed do eiusmod tempor incididunt ut labore et dolore magna aliqua. Ut enim ad minim veniam, quis nostrud exercitation ullamco laboris nisi ut a</p>
    <div class="btn purple">More details</div>
  </article>
</section>

<footer class="abs site-footer"></footer>
<div class="abs address">Rua das Acácias, 148 - Esquina com a Rua Lauro<br>Mendes - Centro - Vila Serena<br><span style="display:block;margin-top:6px">CEP: 55310-240 - Fax: (48) 3555-2917</span></div>
<div class="abs social" aria-label="Social links"><span></span><span></span><span></span><span></span><span></span><span></span></div>
<div class="abs copyright">Copyright 2013 Casalúmen. All Rights reserved.</div>
<div class="abs edition">C2</div>

</body>
</html>
```